Business Card - Apex Wellness

Please use the logo / design elements and font to design a business card that is eye catching and informative. If using "Direct Primary Care" logo element, you don't have to spell it out in the text.

Dr. Brendan Halvik
Apex Wellness - Direct Primary Care
4817 Tillbrook Rd. Suite 305
Fort Smith, AR 72916
Phone: 479-555-0137
ApexWellnessAR.example

```html
<!DOCTYPE html>
<html lang="en">
<head>
<meta charset="utf-8">
<title>Apex Wellness Business Card</title>
<link rel="stylesheet" href="https://fonts.googleapis.com/css2?family=Arimo:wght@400;700&display=swap">
<style>
  :root {
    --backdrop: #e4e4e3;
    --card: #ffffff;
    --navy: #141a45;
    --body-grey: #555555;
    --accent-blue: #2456d6;
  }
  html, body {
    margin: 0;
    padding: 0;
    width: 1200px;
    height: 1200px;
    overflow: hidden;
    background: var(--backdrop);
  }
  .canvas {
    position: relative;
    width: 1200px;
    height: 1200px;
  }
  .card {
    position: absolute;
    width: 688px;
    height: 393px;
    background: var(--card);
    box-shadow: 0 14px 26px rgba(0, 0, 0, 0.18);
  }
  .card-front { left: 267px; top: 159px; }
  .card-back { left: 262px; top: 653px; }

  .identity {
    position: absolute;
    right: 357px;
    top: 160px;
    text-align: right;
    font-family: "Arimo", Arial, sans-serif;
  }
  .identity .person {
    margin: 0;
    font-size: 26px;
    font-weight: 700;
    color: var(--navy);
    line-height: 30px;
    white-space: nowrap;
  }
  .identity .address {
    margin: 3px 0 0;
    font-size: 16px;
    color: var(--body-grey);
    line-height: 21px;
    white-space: nowrap;
  }
  .divider {
    position: absolute;
    left: 347px;
    top: 164px;
    width: 1.5px;
    height: 64px;
    background: var(--navy);
  }
  .contacts {
    position: absolute;
    left: 369px;
    top: 164px;
    margin: 0;
    padding: 0;
    list-style: none;
    font-family: "Arimo", Arial, sans-serif;
    font-size: 16px;
    color: var(--body-grey);
  }
  .contacts li {
    display: flex;
    align-items: center;
    height: 20.5px;
    white-space: nowrap;
  }
  .contacts svg {
    width: 14px;
    height: 14px;
    margin-right: 9px;
    flex: none;
  }

  .brand {
    position: absolute;
    left: 0;
    right: 0;
    top: 130px;
    text-align: center;
  }
  .brand-dot {
    display: block;
    width: 48px;
    height: 48px;
    margin: 0 auto;
    border-radius: 50%;
    background: var(--accent-blue);
  }
  .brand-name {
    margin: 16px 0 0;
    font-family: "Arimo", Arial, sans-serif;
    font-weight: 700;
    font-size: 44px;
    line-height: 52px;
    color: var(--navy);
  }
</style>
</head>
<body>
<main class="canvas">
  <section class="card card-front" aria-label="Business card front">
    <div class="identity">
      <h1 class="person">Dr. Brendan Halvik</h1>
      <p class="address">4817 Tillbrook Rd. Suite 305<br>Fort Smith, AR 72916</p>
    </div>
    <div class="divider"></div>
    <ul class="contacts">
      <li>
        <svg viewBox="0 0 24 24" aria-hidden="true"><path fill="#2456d6" d="M6.6 10.8a15.1 15.1 0 0 0 6.6 6.6l2.2-2.2c.3-.3.7-.4 1-.2 1.1.4 2.3.6 3.6.6.6 0 1 .4 1 1V20c0 .6-.4 1-1 1A17 17 0 0 1 3 4c0-.6.4-1 1-1h3.5c.6 0 1 .4 1 1 0 1.3.2 2.5.6 3.6.1.3 0 .7-.2 1z"/></svg>
        479-555-0137
      </li>
      <li>
        <svg viewBox="0 0 24 24" aria-hidden="true"><rect x="2" y="5" width="20" height="14" rx="1.5" fill="#2456d6"/><path d="M3 6.5l9 6.5 9-6.5" fill="none" stroke="#fff" stroke-width="1.8"/></svg>
        info@apexwellnessar.example
      </li>
      <li>
        <svg viewBox="0 0 24 24" aria-hidden="true"><circle cx="12" cy="12" r="10" fill="#2456d6"/><path d="M7 6c2 1 2 3 4 3s1 3-1 3-2 2-1 4M15 5c-1 2 1 3 3 3M14 14c2 0 3 2 2 4" fill="none" stroke="#fff" stroke-width="1.6"/></svg>
        www.ApexWellnessAR.example
      </li>
    </ul>
  </section>

  <section class="card card-back" aria-label="Business card back">
    <div class="brand">
      <span class="brand-dot"></span>
      <p class="brand-name">Apex Wellness</p>
    </div>
  </section>
</main>
</body>
</html>
```